Devicepickhelper.net needs your creativity!

We need a website design for a new internet company based in Winnipeg MB called devicepickhelper.net. We provide customers who are relatively new to technology a professional intermediary in the computer buying process. We act as an independent purchasing assistant for our customers by getting a clear understanding of their needs and requirements of their machine and proceed to find a computer with the exact specifications they require at the lowest possible price. Because we are completely independent we do not push any particular brand, OS, or software. We want the website to be bold but streamlined, it should be easy to use and navigate even for a beginner.

Target Market(s)

45+ age bracket

Industry/Entity Type

Internet

Requirements
Must have
• The site must have an About Us page, as well as a secure shopping cart where customers can purchase the service via coinvault and credit card. In this section we will require all of the customer's information to be entered as well as what their needs are for their new computer
I would like a product comparison chart that is broken down into three columns where the features of each service can be checked or unchecked depending on each package. I also need an extended service page, where customers will be able to contact me or directly purchase a remote servicing package
Nice to have
• I would like to have an introductory video for the service provided available to customers on the home page so one click and they will be able to see what our service is about.
Should not have
• Do not use any loud audio or sound clips in the design, subtle sound is fine.

```html
<!DOCTYPE html>
<html lang="en">
<head>
<meta charset="utf-8">
<title>Devicepickhelper.net</title>
<link rel="stylesheet" href="https://fonts.googleapis.com/css2?family=Oswald:wght@300;400;500&family=Lobster&family=Roboto:wght@400;700&display=swap">
<style>
:root{
  --nav:#2c3b43;--nav-edge:#1f2a30;--page:#efefef;--ink:#333;--muted:#666;
  --green:#7cb518;--green-dark:#5e9110;--blue:#22a5c6;--blue-dark:#177f9c;
  --olive:#b8b41c;--olive-dark:#929016;--frame:#2f3e46;--card:#fff;
  --footer:#8e96a3;--footer-dark:#3a4850;--footer-bar:#a7aeb9;--link:#1d5fae;
}
*{box-sizing:border-box;margin:0;padding:0}
html,body{width:872px;height:1200px;overflow:hidden}
body{background:var(--page);font-family:Arial,Helvetica,sans-serif;color:var(--ink);position:relative}
.abs{position:absolute}
.topbar{left:0;top:0;width:872px;height:48px;background:var(--nav);border-bottom:2px solid var(--nav-edge)}
.nav{left:100px;top:14px;display:flex;gap:22px;font-family:Oswald,sans-serif;font-size:15px;color:#d9dee1;letter-spacing:.3px}
.nav .active{color:#fff}
.login{left:518px;top:17px;display:flex;gap:5px;align-items:center}
.login .field{width:69px;height:15px;background:#fff;border:1px solid #ccc;font-size:8px;color:#999;padding:2px 8px}
.login .btn{width:47px;height:15px;background:var(--green);color:#fff;font-size:8px;text-align:center;line-height:15px;border-radius:2px}
.login .links{font-size:7px;color:#d9dee1;line-height:10px;margin-left:4px}
.brand{left:101px;top:64px;font-family:Roboto,sans-serif;font-weight:700;font-size:21px;color:#2a2a2a;letter-spacing:1px}
.sales{left:608px;top:66px;font-size:10px;color:#555}
.slider{left:87px;top:105px;width:698px;height:261px;background:var(--frame);border-radius:5px}
.slide-art{left:109px;top:123px;width:656px;height:226px;background:radial-gradient(circle at 70% 40%,#c7e24a,#7fb21c 55%,#4f8a10)}
.arrow{top:218px;width:36px;height:36px;border-radius:50%;background:var(--frame)}
.slide-title{left:144px;top:177px;font-family:Oswald,sans-serif;font-weight:300;font-size:19px;line-height:25px;color:#fff}
.slide-text{left:144px;top:233px;width:210px;font-size:8px;color:#fff;line-height:10px}
.video-btn{left:144px;top:266px;width:128px;height:32px;background:#111;border-radius:4px;color:#fff;font-size:13px;line-height:32px;padding-left:15px}
.card{top:390px;width:218px;height:238px;background:var(--card);border:1px solid #ddd;border-radius:4px}
.card-head{height:51px;background:linear-gradient(#2a2a2a,#000);border-radius:4px 4px 0 0;color:#fff;font-family:Lobster,cursive;font-size:17px;text-align:center;padding-top:8px}
.price{position:absolute;left:28px;top:37px;width:162px;height:28px;color:#fff;font-family:Roboto,sans-serif;font-size:17px;text-align:center;line-height:28px;clip-path:polygon(0 0,100% 0,95% 100%,5% 100%)}
.features{list-style:none;margin:25px 20px 0;font-size:8px;color:#444}
.features li{height:20.5px;line-height:20px;border-bottom:1px solid #eee;padding-left:28px;position:relative}
.features li:last-child{border:none}
.features svg{position:absolute;left:3px;top:4px}
.buy{position:absolute;left:20px;bottom:20px;width:178px;height:28px;border-radius:5px;color:#fff;font-family:Lobster,cursive;font-size:16px;text-align:center;line-height:28px}
.h2{font-family:Lobster,cursive;font-size:17px;color:#222}
.about-art{left:95px;top:680px;width:450px;height:68px;border:3px solid #fff;box-shadow:0 1px 3px rgba(0,0,0,.3);background:linear-gradient(90deg,#6d9f18,#a6cf35 60%,#8dbb22)}
.about-text{left:95px;top:757px;width:450px;font-size:8.5px;line-height:13.5px;color:#333}
.about-text ul{list-style:none;margin:5px 0}
.about-text li{padding-left:10px;position:relative}
.about-text li:before{content:"";position:absolute;left:1px;top:5px;border:2.5px solid transparent;border-left:3px solid #333}
.quote{left:570px;width:210px;font-size:8.5px;line-height:13px;font-style:italic;color:#222;padding-left:13px}
.quote .who{color:var(--link);font-style:italic}
.dash{height:0;border-top:1px dashed #999}
.more{width:70px;height:16px;border-radius:4px;background:linear-gradient(#8ccd2a,#5a9b10);color:#1b3600;font-family:Lobster,cursive;font-size:9px;text-align:center;line-height:16px}
.footer-band{left:0;top:902px;width:872px;height:21px;background:var(--footer-dark)}
.footer{left:0;top:923px;width:872px;height:231px;background:var(--footer)}
.footer-bottom{left:0;top:1154px;width:872px;height:46px;background:var(--footer-bar);border-top:2px dashed #c5cad2}
.fh{font-family:Lobster,cursive;font-size:16px;color:#fff}
.ft{font-size:8.5px;line-height:13.5px;color:#fff}
.ft a{color:#1b4f95;text-decoration:none}
.ft small{font-size:7.5px;color:#333}
.vline{width:0;border-left:1px dashed #b6bcc5;top:954px;height:184px}
.email{left:347px;top:1048px;width:189px;height:20px;background:#f0f0f0;border:1px solid #ddd}
.subscribe{left:347px;top:1081px;width:189px;height:27px;background:linear-gradient(#8ccd2a,#5a9b10);border-radius:3px;color:#fff;font-family:Lobster,cursive;font-size:11px;text-align:center;line-height:27px}
.ci{left:582px;width:30px;height:30px;border-radius:50%;background:#b4bac4}
.cl{left:626px;font-size:11px;color:#fff}
.social{top:1174px;width:15px;height:15px;background:#7d8591;border-radius:2px}
</style>
</head>
<body>
<header class="abs topbar"></header>
<nav class="abs nav"><span class="active">HOME</span><span>ABOUT</span><span>PACKAGES</span><span>TESTIMONIALS</span><span>FAQ</span><span>CONTACT</span></nav>
<div class="abs login"><div class="field">Username</div><div class="field">Password</div><div class="btn">Login</div><div class="links">Forgot Password?<br>Register</div></div>
<div class="abs brand">DEVICEPICKHELPER</div>
<div class="abs sales">24/7 Sales &amp; Support &nbsp; + 1204-555-0148</div>

<section class="abs slider"></section>
<div class="abs arrow" style="left:70px"><svg width="36" height="36"><path d="M17 13l-5 5 5 5" stroke="#ccc" stroke-width="2" fill="none"/></svg></div>
<div class="abs arrow" style="left:766px"><svg width="36" height="36"><path d="M19 13l5 5-5 5" stroke="#ccc" stroke-width="2" fill="none"/></svg></div>
<div class="abs slide-art" role="img" aria-label="Two black computer tower servers on a green bokeh background"></div>
<h1 class="abs slide-title">Device Pick Helper<br>Packages</h1>
<p class="abs slide-text">sit amet, consectetur adipiscing elit. In interdum aliquet orci, vitae ornare erat elementum et.</p>
<div class="abs video-btn">WATCH VIDEO <svg width="12" height="12" style="vertical-align:-1px;margin-left:4px"><path d="M3 1l5 5-5 5" stroke="#fff" stroke-width="2.4" fill="none"/></svg></div>

<article class="abs card" style="left:87px">
  <div class="card-head">Exceptional Value Package</div>
  <div class="price" style="background:var(--blue)">$ 79 / month</div>
  <ul class="features">
    <li><svg width="14" height="12"><path d="M1 6l4 4 8-9" stroke="#4a8a10" stroke-width="2.5" fill="none"/></svg>Hard Disk 120GB</li>
    <li><svg width="14" height="12"><path d="M1 6l4 4 8-9" stroke="#4a8a10" stroke-width="2.5" fill="none"/></svg>VGA 512GHz</li>
    <li><svg width="14" height="12"><path d="M1 6l4 4 8-9" stroke="#4a8a10" stroke-width="2.5" fill="none"/></svg>Wireless Link</li>
    <li><svg width="14" height="12"><path d="M1 6l4 4 8-9" stroke="#4a8a10" stroke-width="2.5" fill="none"/></svg>Dual Core Corelux Processor</li>
    <li><svg width="14" height="12"><path d="M1 6l4 4 8-9" stroke="#4a8a10" stroke-width="2.5" fill="none"/></svg>1 Year Waranty</li>
  </ul>
  <div class="buy" style="background:linear-gradient(#3cc0dd,var(--blue-dark))">Buy Now &nbsp;›</div>
</article>
<article class="abs card" style="left:327px">
  <div class="card-head">Extended Service Package</div>
  <div class="price" style="background:var(--green)">$ 159 / month</div>
  <ul class="features">
    <li><svg width="14" height="12"><path d="M1 6l4 4 8-9" stroke="#4a8a10" stroke-width="2.5" fill="none"/></svg>Hard Disk 120GB</li>
    <li><svg width="14" height="12"><path d="M1 6l4 4 8-9" stroke="#4a8a10" stroke-width="2.5" fill="none"/></svg>VGA 512GHz</li>
    <li><svg width="14" height="12"><path d="M1 6l4 4 8-9" stroke="#4a8a10" stroke-width="2.5" fill="none"/></svg>Wireless Link</li>
    <li><svg width="14" height="12"><path d="M1 6l4 4 8-9" stroke="#4a8a10" stroke-width="2.5" fill="none"/></svg>Dual Core Corelux Processor</li>
    <li><svg width="14" height="12"><path d="M1 6l4 4 8-9" stroke="#4a8a10" stroke-width="2.5" fill="none"/></svg>1 Year Waranty</li>
  </ul>
  <div class="buy" style="background:linear-gradient(#95d132,var(--green-dark))">Buy Now &nbsp;›</div>
</article>
<article class="abs card" style="left:567px">
  <div class="card-head">Full Service Package</div>
  <div class="price" style="background:var(--olive)">$ 95 / month</div>
  <ul class="features">
    <li><svg width="14" height="12"><path d="M1 6l4 4 8-9" stroke="#4a8a10" stroke-width="2.5" fill="none"/></svg>Hard Disk 120GB</li>
    <li><svg width="14" height="12"><path d="M1 6l4 4 8-9" stroke="#4a8a10" stroke-width="2.5" fill="none"/></svg>VGA 512GHz</li>
    <li><svg width="14" height="12"><path d="M1 6l4 4 8-9" stroke="#4a8a10" stroke-width="2.5" fill="none"/></svg>Wireless Link</li>
    <li><svg width="14" height="12"><path d="M1 6l4 4 8-9" stroke="#4a8a10" stroke-width="2.5" fill="none"/></svg>Dual Core Corelux Processor</li>
    <li><svg width="14" height="12"><path d="M1 6l4 4 8-9" stroke="#4a8a10" stroke-width="2.5" fill="none"/></svg>1 Year Waranty</li>
  </ul>
  <div class="buy" style="background:linear-gradient(#cfcb2c,var(--olive-dark))">Buy Now &nbsp;›</div>
</article>

<h2 class="abs h2" style="left:95px;top:645px">About Device Pick Helper</h2>
<div class="abs about-art" role="img" aria-label="Computer tower server on a green background"></div>
<div class="abs about-text">
  <p>Currently the computer buying market offers two distinct, yet underwhelming choices:</p>
  <ul>
    <li>Greatly overpay for a unique and different operating system than you are used to and be left to deal with the numerous challenges of adapting to the new platform</li>
    <li>Pay less for a computer you have been told is great by the green sales associate, only to discover the machine does not meet,or greatly exceeds your needs.</li>
  </ul>
  <p>Now you have a real alternative, a professional in the industry working solely for YOU.</p>
</div>
<div class="abs dash" style="left:95px;top:864px;width:378px"></div>
<div class="abs more" style="left:472px;top:856px">read more</div>

<h2 class="abs h2" style="left:569px;top:645px">Clients Say...</h2>
<div class="abs quote" style="top:677px"><svg class="abs" style="left:0;top:1px" width="8" height="11"><path d="M4 0a4 4 0 0 1 4 4c0 3-4 7-4 7S0 7 0 4a4 4 0 0 1 4-4z" fill="#222"/></svg>Duis aute irure dolor in reprehenderit in voluptate velit esse cillum dolore eu fugiat nulla pariatur. Excepteur sint occaecat cupidatat non proident, sunt in culpa qui officia deserunt mollit anim id est laborum.<br><span style="font-style:normal">~</span> <span class="who">Marisa</span> ~</div>
<div class="abs quote" style="top:765px"><svg class="abs" style="left:0;top:1px" width="8" height="11"><path d="M4 0a4 4 0 0 1 4 4c0 3-4 7-4 7S0 7 0 4a4 4 0 0 1 4-4z" fill="#222"/></svg>Duis aute irure dolor in reprehenderit in voluptate velit esse cillum dolore eu fugiat nulla pariatur. Excepteur sint occaecat cupidatat non proident, sunt in culpa qui officia deserunt mollit anim id est laborum.<br><span style="font-style:normal">~</span> <span class="who">Marisa</span> ~</div>
<div class="abs dash" style="left:569px;top:864px;width:143px"></div>
<div class="abs more" style="left:712px;top:856px">read more</div>

<div class="abs footer-band"></div>
<footer class="abs footer"></footer>
<div class="abs" style="left:110px;top:940px;width:18px;height:18px;border-radius:50%;background:#dfe8f0"></div>
<h3 class="abs fh" style="left:139px;top:939px">Chirper Updates</h3>
<div class="abs ft" style="left:109px;top:975px;width:185px">Nunc tristique mi ac turpis placerat quis sollicitudin metus condimentum. <a>#Donec sed nunc in lacus fermentum ultrices</a> ut eu turpis. Quisque sodales turpis ut risus dignissim non<br><small>10 days ago</small></div>
<div class="abs ft" style="left:109px;top:1057px;width:185px">Nunc tristique mi ac turpis placerat quis sollicitudin metus condimentum. <a>#Donec sed nunc in lacus fermentum ultrices</a> ut eu turpis. Quisque sodales turpis ut risus dignissim non<br><small>10 days ago</small></div>
<div class="abs vline" style="left:318px"></div>
<svg class="abs" style="left:346px;top:942px" width="22" height="16"><rect x="1" y="4" width="18" height="11" rx="2" fill="#e8ecf0"/></svg>
<h3 class="abs fh" style="left:385px;top:939px">Newsletter Signup</h3>
<p class="abs ft" style="left:347px;top:975px;width:190px">Cras volutpat, ante ac gravida iaculis, dui lacus iaculis nibh, eu scelerisque arcu diam a augue. Donec imperdiet pharetra fringilla.</p>
<div class="abs ft" style="left:347px;top:1032px;font-size:8px;color:#333">Your Email Address</div>
<div class="abs email"></div>
<div class="abs subscribe">Subscibe to stay updated with us!</div>
<div class="abs vline" style="left:555px"></div>
<svg class="abs" style="left:581px;top:940px" width="26" height="20"><rect x="6" y="2" width="18" height="13" rx="2" fill="#e8ecf0"/><path d="M2 4c0 8 6 14 14 14l2-3-4-2-2 2c-3-1-5-3-6-6l2-2-2-4z" fill="#333"/></svg>
<h3 class="abs fh" style="left:624px;top:939px">Contact Us</h3>
<div class="abs ci" style="top:976px"><svg width="30" height="30"><path d="M9 13c0-3 12-3 12 0v2h-3v-2h-6v2H9zM10 16h10v6H10z" fill="#7d8591"/></svg></div>
<div class="abs cl" style="top:985px">(012) 555 0190</div>
<div class="abs ci" style="top:1021px"><svg width="30" height="30"><rect x="10" y="9" width="10" height="5" fill="#7d8591"/><rect x="8" y="14" width="14" height="7" rx="1" fill="#7d8591"/></svg></div>
<div class="abs cl" style="top:1030px">(012) 555 0171</div>
<div class="abs ci" style="top:1068px"><svg width="30" height="30"><rect x="8" y="10" width="14" height="10" fill="#efe3a8"/><path d="M8 10l7 5 7-5" stroke="#c9b870" fill="none"/></svg></div>
<div class="abs cl" style="top:1077px">info@devicepickhelper.net</div>

<div class="abs footer-bottom"></div>
<div class="abs" style="left:109px;top:1174px;font-size:8px;color:#555">All Rights Reserved © devicepickhelper.net</div>
<div class="abs fh" style="left:660px;top:1164px">Follow Us</div>
<div class="abs social" style="left:736px"></div>
<div class="abs social" style="left:756px"></div>
</body>
</html>
```